Design and typesetting a BRIV report (approx 8-10 A4 pages)

We are a UK based ideas and innovation agency working within the UK Social Housing sector.
We have a report that needs designing up into an A4 PDF document that should run to about 8-10 A4 pages.
Design-wise we are looking for something dynamic with a housing and tech design theme. The document text is attached in the Word file.
Please find attached our logo and branding guidelines for font and logo use. We would be looking to use the main BRIV purple along with some NEW dynamic complimentary colours used throughout the design.
The report needs to read easily and cleanly so can be spaced out accordingly.
There will be on additional page of text to add at the back which we can send over once the successful candidate has been chosen.
Any questions please ask!
UK Social Housing sector
Social
Other font styles liked:
- Gill Sans for body and Avant Garde for title (as specified in the attached branding guidelines)
- Dynamic feel, stylish, colourful.
- Lots of space around the text.
- A bit of striking design work around the text (in the report template design)
- Cluttered feel and fussy design.

```html
<!DOCTYPE html>
<html lang="en">
<head>
<meta charset="utf-8">
<title>BRIV Digital Housing Report – Spreads</title>
<link href="https://fonts.googleapis.com/css2?family=Cabin:wght@400;600&family=Questrial&display=swap" rel="stylesheet">
<style>
  :root{
    --briv-purple:#5b4fa3;
    --rule-grey:#9a9a9a;
    --ink:#222;
    --muted:#777;
    --paper:#ffffff;
    --backdrop:#b9c9da;
  }
  *{box-sizing:border-box;margin:0;padding:0}
  html,body{width:1200px;height:1200px;overflow:hidden}
  body{background:var(--backdrop);position:relative;font-family:"Cabin",sans-serif;color:var(--ink)}
  .page{position:absolute;width:330px;height:466px;background:var(--paper);overflow:hidden}
  .page--r1{top:58px}.page--r2{top:620px}
  .page--c1{left:73px}.page--c2{left:431px}.page--c3{left:790px}
  .hero{position:absolute;left:0;top:0;width:100%}
  .hero--tall{height:216px}
  .hero--short{height:130px}
  .hero-rule{position:absolute;left:0;top:216px;width:100%;height:6px;background:var(--briv-purple);border-bottom:2px solid var(--rule-grey)}
  .content{position:absolute;left:30px;right:28px}
  .title{font-family:"Questrial",sans-serif;font-weight:400;color:var(--briv-purple);font-size:12.5px;margin-bottom:14px}
  p,li{font-size:5.4px;line-height:1.45;text-align:justify}
  p{margin-bottom:7px}
  ul{list-style:none}
  li{position:relative;padding-left:10px;margin-bottom:5px}
  li::before{content:"";position:absolute;left:0;top:1.5px;width:3px;height:3px;background:var(--briv-purple)}
  .contact-note{font-size:7px;color:var(--muted);margin-top:6px}
  .footer{position:absolute;left:0;bottom:0;width:100%;height:50px}
  .footer-rule{position:absolute;left:0;right:0;top:26px;height:5px;background:var(--briv-purple);border-bottom:2px solid var(--rule-grey)}
  .brand{position:absolute;left:26px;top:18px;background:var(--paper);padding:0 8px 0 4px;display:flex;align-items:center;gap:5px;height:18px}
  .brand-mark{width:7px;height:7px;background:var(--briv-purple)}
  .brand-name{font-family:"Cabin",sans-serif;font-weight:400;font-size:12px;color:var(--briv-purple);line-height:1}
  .folio{position:absolute;right:22px;top:8px;width:18px;height:18px;background:var(--briv-purple);color:#fff;font-size:6px;display:flex;align-items:center;justify-content:center}
  .back-panel{position:absolute;left:0;top:182px;width:100%;height:218px;background:var(--briv-purple);color:#fff;text-align:center}
  .back-grey{position:absolute;left:0;top:400px;width:100%;height:66px;background:var(--rule-grey)}
  .back-brand{position:absolute;left:0;right:0;top:132px;display:flex;justify-content:center;align-items:center;gap:5px}
  .back-brand .brand-name{color:#fff;font-size:14px}
  .back-brand .brand-mark{background:#fff}
  .back-contact{position:absolute;left:0;right:0;top:164px;font-size:7.5px;line-height:1.45}
</style>
</head>
<body>

<section class="page page--r1 page--c1">
  <div class="hero hero--tall" role="img" aria-label="Digital house outline over glowing blue circuit board" style="background:radial-gradient(circle at 55% 40%,#9fc4ff 0%,#4d63d6 35%,#2b2d8f 75%,#1d1f63 100%)"></div>
  <div class="hero-rule"></div>
  <div class="content" style="top:238px">
    <h2 class="title">How far could digital housing providers go?</h2>
    <p>What is frustrating about the current state of housing technology is that – outside of housing – the business models, understanding and tools exist to radically rethink how housing businesses might be delivered. The opportunity is there to radically transform business models using existing technology. The question is not whether but how far the more effective deployment of technology could allow housing providers to go in delivering radically better services in a much more challenging resource environment.</p>
    <p>Could we create a housing provider with only a very few staff managing a platform for tenants to self-manage their own properties? Or a business driven by comprehensive, accurate real-time information driving resource deployment and business decisions? Do we need to be reliant on conventional housing management system-based IT infrastructure? A few years ago no-one could have imagined ChatterMobile or Nestly or Ridewell. Looking closer to home, Northern Heat's FlameSense product stands ready to revolutionise housing how boiler servicing and repairs are delivered.</p>
  </div>
  <footer class="footer"><div class="footer-rule"></div><div class="brand"><span class="brand-mark"></span><span class="brand-name">BRIV</span></div><span class="folio">7</span></footer>
</section>

<section class="page page--r1 page--c2">
  <div class="hero hero--short" role="img" aria-label="Hands typing on a silver laptop keyboard" style="background:linear-gradient(120deg,#e9e9ea 0%,#c9cacd 45%,#8e9096 75%,#3b3d42 100%)"></div>
  <div class="content" style="top:163px">
    <p>As business starts to preparing for the "post-app era" defined by intelligent agents, cloud based bots and learning algorithms, why are housing providers are still focused on channel shift and mobilizing conventional workforces? With machine learning and AI now accessible to almost everyone who wants to explore and/or deploy it, why are housing providers still struggling to make sense of inadequate data poorly managed across multiple systems, some of them rooted in the 1980s and 90s?</p>
    <p>Housing has the opportunity to radically reassess its relationship with data and technology. But it doesn't have the people or the tools, particularly at the top of its businesses. The starting point for addressing that gap is to ensure technology and data are owned across board tables and on senior executive teams.</p>
    <p>For the last 15 years we have seen housing providers pushed to get financial and development expertise on their boards and increasing numbers of finance professionals taking on CEO positions in landlord businesses. This has driven rapid and exciting innovation in funding and finance raising across the sector and a step change in approaches to development.</p>
    <p>The challenge the sector now faces is to recognise and invest in effective digital leadership and governance as a first step to delivering digital transformation across their businesses.</p>
  </div>
  <footer class="footer"><div class="footer-rule"></div><div class="brand"><span class="brand-mark"></span><span class="brand-name">BRIV</span></div><span class="folio">8</span></footer>
</section>

<section class="page page--r1 page--c3">
  <div class="hero hero--tall" role="img" aria-label="Businessman's open hand holding a glowing house symbol" style="background:radial-gradient(circle at 58% 45%,#7fa9d6 0%,#2d4f78 30%,#14243a 70%,#0b1420 100%)"></div>
  <div class="hero-rule"></div>
  <div class="content" style="top:240px">
    <h2 class="title">How do we start to fix it?</h2>
    <p>BRIV believes that change needs to start at Board level. That is why we are delighted to be partnering with technology industry body DigiNation and leading digital recruitment specialists Marlow Kestrel to launched a major initiative aimed at placing leading players from the UK's digital economy on every housing provider board, committing to helping UK housing bridge its "digital governance gap".</p>
    <p>The initiative will:</p>
    <ul>
      <li>match digital leaders from across the UK technology sector with housing provider boards, delivering a significant increase in digital capability at governance level at a time when digital transformation is becoming an increasingly important issue for many landlords</li>
      <li>provide full onboarding support, helping new board members understand the challenges and opportunities within the housing sector, and maximising their ability to succeed in their new housing roles.</li>
      <li>establish of a network of tech-focused housing association board members to ensure that housing provider boards are equipt to engage with the major digital transformation challenges that will face all housing businesses now and in the future.</li>
    </ul>
    <p class="contact-note">For more information contact xxxxxxx</p>
  </div>
  <footer class="footer"><div class="footer-rule"></div><div class="brand"><span class="brand-mark"></span><span class="brand-name">BRIV</span></div><span class="folio">9</span></footer>
</section>

<section class="page page--r2 page--c1">
  <div class="hero hero--tall" role="img" aria-label="Modern detached house lit up at dusk with lawn and path" style="background:linear-gradient(180deg,#1f3150 0%,#34507a 40%,#6b5a45 68%,#3d4a2a 100%)"></div>
  <div class="hero-rule"></div>
  <div class="content" style="top:244px">
    <h2 class="title">Longer term</h2>
    <p style="margin-bottom:10px">Longer term, there is a need for UK housing to significantly increase its digital maturity, focusing in particular on</p>
    <ul>
      <li>digital literacy and leadership</li>
      <li>attitudes to technology-led expenditure</li>
      <li>approach to tech innovation</li>
      <li>awareness of and/or understanding of the latest technology trends and opportunities</li>
      <li>the use of data to drive business decisions and inform new and more relevant customer focused strategies</li>
    </ul>
  </div>
  <footer class="footer"><div class="footer-rule"></div><div class="brand"><span class="brand-mark"></span><span class="brand-name">BRIV</span></div><span class="folio">10</span></footer>
</section>

<section class="page page--r2 page--c2">
  <div class="hero hero--short" role="img" aria-label="Couple seen from behind looking at a new brick apartment building" style="background:linear-gradient(90deg,#c7a58a 0%,#b98b6a 35%,#8a6650 60%,#e8e2da 100%)"></div>
  <div class="content" style="top:164px">
    <p style="margin-bottom:9px">Housing providers need to:</p>
    <ul>
      <li>reframe housing technology as a core driver of the radical business transformation landlords will need to deliver over the next 3-4 years</li>
      <li>understand that the challenge is not just one of making existing systems marginally more efficient through channel shift and mobilisation of workforces but more comprehensively reinvent how business is delivered</li>
      <li>move rapidly towards consideration of the case for CTO and/or CDO roles as a core part of every senior executive team</li>
      <li>continue to recruit board members from technology-savvy businesses, with the UK e-commerce and technology sector industries increasingly broad and mature, there is a large potential pool of talent to be drawn on.</li>
    </ul>
    <p style="margin-top:8px">In early 2017, BRIV will be launching a full Digital Maturity Audit of housing provider businesses, seeking to benchmark housing providers' existing digital capability and their readiness to deliver digital change in the future.</p>
    <p class="contact-note">For more information contact xxxxxxx</p>
  </div>
  <footer class="footer"><div class="footer-rule"></div><div class="brand"><span class="brand-mark"></span><span class="brand-name">BRIV</span></div><span class="folio">11</span></footer>
</section>

<section class="page page--r2 page--c3">
  <div class="hero" style="height:182px;background:linear-gradient(135deg,#cfe6f7 0%,#7fb2dc 40%,#2f5f9a 75%,#1b3766 100%)" role="img" aria-label="Pixelated house icon on a blue digital screen"></div>
  <div class="back-panel">
    <div class="back-brand"><span class="brand-mark"></span><span class="brand-name">BRIV</span></div>
    <div class="back-contact">0207 946 0132<br>12-14 Fenton Row, London, E2 7QX<br>@BRIVhousing</div>
  </div>
  <div class="back-grey"></div>
</section>

</body>
</html>
```